Weight loss surgery restaurant card

We need to create a card for patients who have undergone weight loss surgery to take to restaurants so they can request smaller meals. These patients have had surgery on their stomach so that they can only consume half to one cup of food at a time. So normal sized restaurant meals are way too big (and cost a lot). This card they can present to the restaurant to communicate the fact that they have had weight loss surgery and therefore request a smaller meal portion at reduced cost

Target Market(s)

Restaurants serving weight loss surgery patients

Industry/Entity Type

Health Care

Contact Information for Business Card

This will be a plastic card similar to business card size.

Requirements
Must have
• The front of the card should include the following text:
• The individual bearing this card has undergone weight loss surgery.
• This surgery restricts portion sizes to between half and one cup of food at a time.
• Please give consideration to allowing smaller portions of your regular meals to be ordered to reduce wastage and excess costs.
• Example: a half size portion priced at two thirds of usual cost.
• The back of the card will have spaces for the person to write certain information. These are the categories that can be filled in by hand:
• Name:
• Procedure performed:
• Date of procedure (month/year):
• Treating Clinic Name:
• Treating Clinic Signature:
• Somewhere down the bottom should be something along the lines of:
• supplied from bernardwhitlow.com.au
Nice to have
• A nice design with imagery/colours etc ... not just the text on a white background! Bright attractive colours preferred.
• I have uploaded my logo ... a roughly triangular image followed by my name etc. The triangular logo image could be used somewhere on the card and this logo can be interchangeable for other clinics who purchase the card.
• **Please note that I don't want my name to be included as part of the logo on the card ... just use the triangular image on the side of the logo without the following name**
• Also, the colouring of the card does not have to reflect my logo colours as I am anticipating interchanging this logo with other logos if other clinics choose to adopt the card. I am interested to see other, more generic, colour choices as well as my logo colours

```html
<!DOCTYPE html>
<html lang="en">
<head>
<meta charset="utf-8">
<title>Weight Loss Surgery Restaurant Card</title>
<link rel="stylesheet" href="https://fonts.googleapis.com/css2?family=Ubuntu:wght@700&family=Roboto+Condensed:wght@300;400;700&display=swap">
<style>
  :root {
    --teal: #14897f;
    --teal-deep: #0f7068;
    --teal-soft: #8cc3bd;
    --teal-mist: #dcedeb;
    --grey-head: #727375;
    --grey-note: #7d7f82;
    --plate: #eceeed;
    --white: #ffffff;
  }
  html, body {
    margin: 0;
    padding: 0;
    width: 1056px;
    height: 1200px;
    overflow: hidden;
    background: var(--white);
  }
  .sheet {
    position: relative;
    width: 1056px;
    height: 1200px;
    font-family: "Roboto Condensed", sans-serif;
  }
  .card {
    position: absolute;
    left: 88px;
    width: 880px;
    height: 505px;
    overflow: hidden;
    box-shadow: 0 2px 6px rgba(0,0,0,0.25);
  }
  .card--front {
    top: 80px;
    background: linear-gradient(100deg, var(--white) 42%, #eef6f5 62%, var(--teal-mist) 78%, var(--teal-soft) 100%);
  }
  .card--back {
    top: 626px;
  }

  /* Front */
  .food-photo {
    position: absolute;
    left: 0;
    top: 0;
    width: 300px;
    height: 318px;
    border-bottom-right-radius: 300px 318px;
    background: radial-gradient(circle at 40% 45%, #e9b36a 0%, #f3d9a8 30%, #faf3e6 62%, #f6f1e8 100%);
  }
  .fork-photo {
    position: absolute;
    left: 812px;
    top: 228px;
    width: 46px;
    height: 277px;
    background: linear-gradient(90deg, rgba(120,120,115,0.15), rgba(160,160,150,0.55), rgba(120,120,115,0.15));
    border-radius: 18px 18px 4px 4px;
  }
  .headline {
    position: absolute;
    left: 344px;
    top: 56px;
    margin: 0;
    font-family: "Ubuntu", sans-serif;
    font-weight: 700;
    font-size: 44px;
    line-height: 43px;
    color: var(--teal);
    letter-spacing: -0.3px;
  }
  .headline span { display: block; }
  .headline .headline__tail { color: var(--grey-head); }
  .facts {
    position: absolute;
    left: 332px;
    top: 216px;
    margin: 0;
    padding: 0;
    list-style: none;
    width: 520px;
  }
  .facts li {
    position: relative;
    padding-left: 18px;
    font-size: 25px;
    line-height: 26px;
    font-weight: 300;
    color: var(--teal);
    margin-bottom: 12px;
  }
  .facts li::before {
    content: "";
    position: absolute;
    left: 0;
    top: 8px;
    width: 10px;
    height: 10px;
    border-radius: 50%;
    background: var(--teal);
  }
  .facts strong { font-weight: 700; }
  .example-note {
    position: absolute;
    left: 350px;
    top: 432px;
    margin: 0;
    font-size: 17px;
    font-weight: 300;
    color: var(--grey-note);
  }
  .brand {
    position: absolute;
    display: flex;
    align-items: center;
    gap: 10px;
    color: var(--teal);
  }
  .brand__dot {
    width: 34px;
    height: 34px;
    border-radius: 50%;
    background: var(--teal);
    flex: none;
  }
  .brand__text { display: flex; flex-direction: column; }
  .brand__name {
    font-size: 25px;
    line-height: 24px;
    font-weight: 400;
    text-transform: uppercase;
    letter-spacing: 1px;
  }
  .brand__role {
    font-size: 9px;
    line-height: 11px;
    font-weight: 400;
    text-transform: uppercase;
    letter-spacing: 1.2px;
  }
  .card--front .brand { left: 32px; top: 418px; }

  /* Back */
  .table-photo {
    position: absolute;
    inset: 0;
    background:
      radial-gradient(ellipse 560px 500px at 210px 470px, #f4f5f4 0%, var(--plate) 55%, #dfe3e1 70%, transparent 71%),
      linear-gradient(100deg, #f0f2f1 30%, #d7e7e4 65%, #7fb3ad 100%);
  }
  .knife-photo {
    position: absolute;
    left: 702px;
    top: 104px;
    width: 60px;
    height: 401px;
    border-radius: 30px 30px 6px 6px;
    background: linear-gradient(90deg, rgba(150,150,145,0.25), rgba(200,200,195,0.75), rgba(150,150,145,0.3));
  }
  .card--back .brand { left: 540px; top: 48px; }
  .fields {
    position: absolute;
    left: 54px;
    top: 182px;
    margin: 0;
    padding: 0;
    list-style: none;
    width: 578px;
  }
  .fields li {
    position: relative;
    height: 44px;
    margin-bottom: 2px;
    padding-left: 28px;
    font-size: 29px;
    line-height: 44px;
    font-weight: 300;
    color: var(--teal);
    background: linear-gradient(90deg, rgba(255,255,255,0.25), rgba(255,255,255,0.75) 60%, rgba(255,255,255,0.3));
    border-bottom: 2px solid rgba(190,196,194,0.7);
  }
  .fields li::before {
    content: "";
    position: absolute;
    left: 4px;
    top: 17px;
    width: 10px;
    height: 10px;
    border-radius: 50%;
    background: var(--teal);
  }
  .fields__slash {
    position: absolute;
    left: 456px;
    top: 0;
  }
  .supplier {
    position: absolute;
    left: 86px;
    top: 432px;
    margin: 0;
    font-size: 30px;
    font-weight: 300;
    color: var(--teal);
  }
  .supplier__url { color: var(--grey-note); }
</style>
</head>
<body>
<main class="sheet">

  <section class="card card--front" aria-label="Card front">
    <div class="food-photo" role="img" aria-label="Photo of a plate with a pancake topped with kiwi fruit and blueberries, lemon wedges beside it"></div>
    <div class="fork-photo" role="img" aria-label="Photo of a silver fork"></div>

    <h1 class="headline">
      <span>the individual bearing</span>
      <span>this card has undergone</span>
      <span class="headline__tail">weight loss surgery</span>
    </h1>

    <ul class="facts">
      <li>Around <strong>500,000</strong> of these procedures are performed around the world every year.</li>
      <li>This surgery restricts portion sizes to between <strong>half and one cup</strong> of food at a time.</li>
      <li>Please give consideration to allowing <strong>smaller portions</strong> of your regular meals to be ordered to <strong>reduce wastage</strong> and <strong>excess costs</strong>.</li>
    </ul>
    <p class="example-note">For example: a half size portion priced at two thirds of usual cost.</p>

    <div class="brand">
      <span class="brand__dot"></span>
      <span class="brand__text">
        <span class="brand__name">Bernard Whitlow</span>
        <span class="brand__role">General, Upper GI &amp; Bariatric Surgeon</span>
      </span>
    </div>
  </section>

  <section class="card card--back" aria-label="Card back">
    <div class="table-photo" role="img" aria-label="Photo of an empty white dinner plate on a pale teal table"></div>
    <div class="knife-photo" role="img" aria-label="Photo of a silver table knife"></div>

    <div class="brand">
      <span class="brand__dot"></span>
      <span class="brand__text">
        <span class="brand__name">Bernard Whitlow</span>
        <span class="brand__role">General, Upper GI &amp; Bariatric Surgeon</span>
      </span>
    </div>

    <ul class="fields">
      <li>Name:</li>
      <li>Procedure performed:</li>
      <li>Date of procedure (month/year):<span class="fields__slash">/</span></li>
      <li>Treating Clinic Name:</li>
      <li>Treating Clinic Signature:</li>
    </ul>

    <p class="supplier">Purchased through <span class="supplier__url">www.bernardwhitlow.com.au</span></p>
  </section>

</main>
</body>
</html>
```